Tor'k Wayfarer Travel

We need a sleek, professional, inviting card to elicit global travel for the experienced and professional traveler. Royal blue, black and silver. (perhaps the wording could be silver with black shadow?-get creative) Maybe a watermark on the front and the full raised logo on the back.
We want a stylish and modern card, but professional.

```html
<!DOCTYPE html>
<html lang="en">
<head>
<meta charset="utf-8">
<title>Tor'k Wayfarer Travel – Business Card</title>
<link href="https://fonts.googleapis.com/css2?family=Arimo:wght@400;700&family=Montserrat:wght@700&display=swap" rel="stylesheet">
<style>
  :root {
    --backdrop: #e4e4e2;
    --card: #2c2c2c;
    --card-deep: #212121;
    --brand-blue: #1f9fd8;
    --brand-green: #6cae2c;
    --text-light: #e8e8e8;
    --rule: #cfcfcf;
    --silver-hi: rgba(170,170,170,0.55);
    --silver-lo: rgba(90,90,90,0.25);
  }
  * { margin: 0; padding: 0; box-sizing: border-box; }
  html, body { width: 1200px; height: 801px; overflow: hidden; }
  body {
    background: var(--backdrop);
    font-family: "Arimo", Arial, sans-serif;
    display: flex;
    align-items: center;
    justify-content: center;
    gap: 40px;
  }
  .card {
    position: relative;
    width: 560px;
    height: 320px;
    background: linear-gradient(160deg, var(--card) 0%, var(--card-deep) 100%);
    border-bottom: 5px solid var(--brand-green);
    border-left: 3px solid var(--brand-green);
    box-shadow: 0 14px 30px rgba(0,0,0,0.25);
    overflow: hidden;
  }
  .brand-name {
    font-family: "Montserrat", Arial, sans-serif;
    font-weight: 700;
    color: var(--brand-blue);
    letter-spacing: 1px;
    text-transform: uppercase;
    white-space: nowrap;
  }
  .brand-rule {
    height: 2px;
    background: var(--brand-green);
  }

  /* Front card */
  .front .brand {
    position: absolute;
    top: 60px;
    left: 240px;
    width: 290px;
    text-align: center;
  }
  .front .brand-name { font-size: 21px; }
  .front .brand-rule { margin: 8px auto 0; width: 270px; }
  .front .address {
    position: absolute;
    right: 36px;
    top: 150px;
    text-align: right;
    color: var(--text-light);
    font-size: 13px;
    line-height: 1.35;
  }
  .front .holder {
    position: absolute;
    left: 36px;
    top: 166px;
  }
  .holder-name {
    color: var(--brand-green);
    font-weight: 700;
    font-size: 22px;
    line-height: 1.1;
  }
  .holder-role {
    color: var(--text-light);
    font-size: 14px;
    margin-top: 3px;
  }
  .front .divider {
    position: absolute;
    left: 36px;
    right: 36px;
    top: 220px;
    height: 1px;
    background: var(--rule);
  }
  .contacts {
    position: absolute;
    left: 36px;
    top: 230px;
    list-style: none;
  }
  .contacts li {
    display: flex;
    align-items: center;
    gap: 10px;
    color: var(--text-light);
    font-size: 14px;
    height: 22px;
  }
  .contact-icon {
    width: 17px;
    height: 17px;
    border-radius: 4px;
    background: var(--brand-green);
    display: flex;
    align-items: center;
    justify-content: center;
    flex: none;
  }
  .contact-icon svg { width: 11px; height: 11px; }
  .accent { color: var(--brand-green); }

  /* Back card */
  .back .watermark {
    position: absolute;
    left: 190px;
    top: 26px;
    width: 190px;
    height: 190px;
    border-radius: 50%;
    background: radial-gradient(circle at 35% 30%, var(--silver-hi) 0%, var(--silver-lo) 70%, rgba(60,60,60,0.1) 100%);
    box-shadow: inset -6px -8px 14px rgba(0,0,0,0.35);
  }
  .back .brand {
    position: absolute;
    left: 130px;
    top: 232px;
    width: 380px;
    text-align: center;
  }
  .back .brand-name { font-size: 26px; }
  .back .brand-rule { margin: 10px auto 0; width: 360px; }
</style>
</head>
<body>
  <section class="card front" aria-label="Business card front">
    <div class="brand">
      <span class="brand-name">Tor'k Wayfarer Travel</span>
      <div class="brand-rule"></div>
    </div>
    <p class="address">Your address, city<br>state, ZIP 0000</p>
    <div class="holder">
      <p class="holder-name">Marcus Bellamy</p>
      <p class="holder-role">Manager</p>
    </div>
    <div class="divider"></div>
    <ul class="contacts">
      <li>
        <span class="contact-icon">
          <svg viewBox="0 0 24 24"><path fill="#fff" d="M6.6 10.8a15 15 0 0 0 6.6 6.6l2.2-2.2a1 1 0 0 1 1-.25 11.4 11.4 0 0 0 3.6.57 1 1 0 0 1 1 1V20a1 1 0 0 1-1 1A17 17 0 0 1 3 4a1 1 0 0 1 1-1h3.5a1 1 0 0 1 1 1c0 1.25.2 2.45.57 3.57a1 1 0 0 1-.25 1z"/></svg>
        </span>
        <span>555-014-2100</span>
      </li>
      <li>
        <span class="contact-icon">
          <svg viewBox="0 0 24 24"><rect x="2" y="5" width="20" height="14" fill="none" stroke="#fff" stroke-width="2"/><path d="M2 5l10 8 10-8" fill="none" stroke="#fff" stroke-width="2"/></svg>
        </span>
        <span>hello@torkmail.com</span>
      </li>
      <li>
        <span class="contact-icon">
          <svg viewBox="0 0 24 24"><circle cx="12" cy="12" r="9" fill="none" stroke="#fff" stroke-width="2"/><path d="M3 12h18M12 3c3 3 3 15 0 18M12 3c-3 3-3 15 0 18" fill="none" stroke="#fff" stroke-width="1.6"/></svg>
        </span>
        <span>www.<span class="accent">torkwayfarer</span>.com</span>
      </li>
    </ul>
  </section>

  <section class="card back" aria-label="Business card back">
    <div class="watermark" role="img" aria-label="Raised silver brand emblem area"></div>
    <div class="brand">
      <span class="brand-name">Tor'k Wayfarer Travel</span>
      <div class="brand-rule"></div>
    </div>
  </section>
</body>
</html>
```